Business Card Design Project

We discover connections between taxi drivers and passengers, improve service quality and save time for both parties.
We need a business card design for a mobile applications company in Melbourne called Hop Along Rides.
Our initial application - HopAlongRides - has taxi and passenger parts, and as such there has to be some sort of link between cab colors (gold/yellow and black) and passengers. Passenger color can be chosen at will and be in harmony with cab colors. Card should also include a symbol of mobile technology such as mobile phone, wireless signal or something else that people associate with mobile applications. Final design should communicate connection between taxis and passengers that is created or refers to mobile phone or tablet (mobile technologies).
Keep in mind that we need a logo as part of the design.
Winning design will be favoured for our next designs that will be posted here!

Target Market(s)

taxi drivers, businessmen/businesswomen, entrepreneurs, contractors, ceos, executives

Industry/Entity Type

Taxi

Requirements
Must have
• This is a product business card, not a personal business card. Therefore it has to include product logo, a slogan under product name and links to social networks - plain circle, Pagebook, contact e-mail address and website link with corresponding icons.
Reference to taxi/cab and passenger businesslike figure with variations of male and female.
Reference to mobile technologies such as phone, tablet or mobile connectivity.
Card must be designed and have an exact fit for 1039 x 697 pixels (300dpi)

```html
<!DOCTYPE html>
<html lang="en">
<head>
<meta charset="utf-8">
<title>Hop Along Rides – Business Card</title>
<link rel="stylesheet" href="https://fonts.googleapis.com/css2?family=Russo+One&family=Arimo:wght@400&display=swap">
<style>
  :root {
    --card-black: #000000;
    --cab-yellow: #ffe600;
    --cab-yellow-deep: #e8c800;
    --text-white: #ffffff;
    --band-light: #e6e6e6;
    --band-dark: #8a8a8a;
    --social-blue: #1f4fa8;
    --social-mint: #6fe0c2;
    --slogan-blue: #c9d9ff;
    --slogan-glow: #ff9ee0;
  }
  html, body {
    margin: 0;
    padding: 0;
    width: 1200px;
    height: 803px;
    overflow: hidden;
    background: var(--card-black);
  }
  .card {
    position: relative;
    width: 1200px;
    height: 803px;
    background: var(--card-black);
    font-family: "Arimo", Arial, sans-serif;
    color: var(--text-white);
    overflow: hidden;
  }
  .card__band {
    position: absolute;
    left: 0;
    top: 208px;
    width: 1200px;
    height: 101px;
    background: linear-gradient(90deg, var(--band-light), var(--band-dark) 50%, var(--band-light));
  }
  .card__sign {
    position: absolute;
    left: 55px;
    top: 12px;
    width: 271px;
    height: 224px;
    background: linear-gradient(180deg, var(--cab-yellow), var(--cab-yellow-deep));
    border-radius: 6px;
  }
  .card__wordmark {
    position: absolute;
    left: 380px;
    top: 98px;
    width: 790px;
    margin: 0;
    text-align: center;
    font-family: "Russo One", "Arial Black", sans-serif;
    font-weight: 400;
    font-size: 96px;
    line-height: 1;
    color: var(--text-white);
  }
  .card__email {
    position: absolute;
    right: 49px;
    top: 326px;
    margin: 0;
    font-size: 44px;
    line-height: 1;
  }
  .social {
    position: absolute;
    left: 52px;
    margin: 0;
    display: flex;
    align-items: center;
    gap: 6px;
    font-size: 44px;
    line-height: 1;
  }
  .social--page { top: 416px; }
  .social--tag { top: 511px; }
  .social__dot {
    width: 84px;
    height: 84px;
    border-radius: 50%;
    flex: none;
  }
  .social--page .social__dot { background: var(--social-blue); }
  .social--tag .social__dot { background: var(--social-mint); }
  .card__web {
    position: absolute;
    right: 49px;
    top: 511px;
    height: 84px;
    margin: 0;
    display: flex;
    align-items: center;
    gap: 12px;
    font-size: 44px;
    line-height: 1;
  }
  .card__web-icon {
    width: 34px;
    height: 56px;
    flex: none;
  }
  .card__slogan {
    position: absolute;
    left: 0;
    top: 648px;
    width: 1200px;
    margin: 0;
    text-align: center;
    font-size: 55px;
    line-height: 72px;
    color: var(--slogan-blue);
    text-shadow: 0 0 2px var(--slogan-glow), 0 0 2px var(--slogan-glow);
  }
</style>
</head>
<body>
  <main class="card">
    <div class="card__band" role="img" aria-label="Black and white chequered taxi band"></div>
    <div class="card__sign" role="img" aria-label="Yellow taxi roof sign with rising mobile signal bars"></div>
    <h1 class="card__wordmark">HopAlongRides</h1>
    <p class="card__email">email: info@hopalongrides.net</p>
    <p class="social social--page"><span class="social__dot"></span>http://www.pagebook.com/hopalongrides</p>
    <p class="social social--tag"><span class="social__dot"></span>#hopalongrides</p>
    <p class="card__web">
      <svg class="card__web-icon" viewBox="0 0 34 56" aria-hidden="true">
        <rect x="2" y="2" width="30" height="52" rx="5" fill="none" stroke="#ffffff" stroke-width="3"/>
        <line x1="12" y1="8" x2="22" y2="8" stroke="#ffffff" stroke-width="2.5" stroke-linecap="round"/>
        <circle cx="17" cy="46" r="3" fill="#ffffff"/>
      </svg>
      www.hopalongrides.net
    </p>
    <p class="card__slogan">Connecting Taxi Drivers and Passengers<br>to Save You Time</p>
  </main>
</body>
</html>
```